Answer Choice Icons

We need four versions of an answer choice icon. We need an A, B, C and D. They need to be 40 by 40 pixels and in .png format. They will be used as the labels for the answer choices on a multiple choice test. The student will click on the A, the B, the C, or D icon to select their answer. I have uploaded an example.

Industry/Entity Type

Student

Requirements
Must have
• 40 x 40 pixels; png format
Nice to have
• An oval shape with some shine would be nice. Also having each one a different color would be good.

```html
<!DOCTYPE html>
<html lang="en">
<head>
<meta charset="utf-8">
<title>Answer Choice Icons</title>
<link href="https://fonts.googleapis.com/css2?family=Open+Sans:wght@600&display=swap" rel="stylesheet">
<style>
  :root {
    --page-bg: #ffffff;
    --text: #1b1b1b;
    --blue-ring: #0b67d0;
    --blue-light: #8ad8ff;
    --blue-mid: #2fa4f0;
    --blue-letter: #1b3f9e;
    --yellow-ring: #c4a400;
    --yellow-light: #fff9a0;
    --yellow-mid: #f0dc1a;
    --yellow-letter: #86681a;
    --green-ring: #0a820a;
    --green-light: #8cf08c;
    --green-mid: #27c027;
    --green-letter: #1d531d;
    --red-ring: #c40606;
    --red-light: #ffb0b0;
    --red-mid: #f04848;
    --red-letter: #7e1010;
  }
  html, body {
    margin: 0;
    padding: 0;
    width: 1200px;
    height: 900px;
    overflow: hidden;
    background: var(--page-bg);
  }
  .slide {
    position: relative;
    width: 1200px;
    height: 900px;
    font-family: "Open Sans", "Segoe UI", sans-serif;
    font-weight: 600;
    color: var(--text);
  }
  .question {
    position: absolute;
    left: 91px;
    top: 175px;
    margin: 0;
    font-size: 29px;
    line-height: 1.2;
    font-weight: 600;
  }
  .choices {
    position: absolute;
    left: 151px;
    top: 365px;
    margin: 0;
    padding: 0;
    list-style: none;
  }
  .choice {
    display: flex;
    align-items: center;
    height: 40px;
    margin-bottom: 20px;
  }
  .choice-icon {
    width: 64px;
    height: 40px;
    flex: none;
  }
  .choice-label {
    margin-left: 26px;
    font-size: 29px;
    line-height: 40px;
  }
  .icon-letter {
    font-family: "Open Sans", sans-serif;
    font-size: 24px;
    font-weight: 600;
  }
</style>
</head>
<body>
<main class="slide">
  <h1 class="question">Question: Here is a question</h1>

  <ul class="choices">
    <li class="choice">
      <svg class="choice-icon" viewBox="0 0 64 40" aria-hidden="true">
        <defs>
          <radialGradient id="fill-a" cx="50%" cy="40%" r="60%">
            <stop offset="0" stop-color="var(--blue-light)"/>
            <stop offset="1" stop-color="var(--blue-mid)"/>
          </radialGradient>
        </defs>
        <ellipse cx="32" cy="20" rx="31" ry="19" fill="var(--blue-ring)"/>
        <ellipse cx="32" cy="19" rx="26" ry="15" fill="url(#fill-a)"/>
        <ellipse cx="32" cy="12" rx="19" ry="6" fill="#ffffff" opacity="0.55"/>
        <text class="icon-letter" x="32" y="28" text-anchor="middle" fill="var(--blue-letter)">A</text>
      </svg>
      <span class="choice-label">Answer 1</span>
    </li>
    <li class="choice">
      <svg class="choice-icon" viewBox="0 0 64 40" aria-hidden="true">
        <defs>
          <radialGradient id="fill-b" cx="50%" cy="40%" r="60%">
            <stop offset="0" stop-color="var(--yellow-light)"/>
            <stop offset="1" stop-color="var(--yellow-mid)"/>
          </radialGradient>
        </defs>
        <ellipse cx="32" cy="20" rx="31" ry="19" fill="var(--yellow-ring)"/>
        <ellipse cx="32" cy="19" rx="26" ry="15" fill="url(#fill-b)"/>
        <ellipse cx="32" cy="12" rx="19" ry="6" fill="#ffffff" opacity="0.55"/>
        <text class="icon-letter" x="32" y="28" text-anchor="middle" fill="var(--yellow-letter)">B</text>
      </svg>
      <span class="choice-label">Answer 2</span>
    </li>
    <li class="choice">
      <svg class="choice-icon" viewBox="0 0 64 40" aria-hidden="true">
        <defs>
          <radialGradient id="fill-c" cx="50%" cy="40%" r="60%">
            <stop offset="0" stop-color="var(--green-light)"/>
            <stop offset="1" stop-color="var(--green-mid)"/>
          </radialGradient>
        </defs>
        <ellipse cx="32" cy="20" rx="31" ry="19" fill="var(--green-ring)"/>
        <ellipse cx="32" cy="19" rx="26" ry="15" fill="url(#fill-c)"/>
        <ellipse cx="32" cy="12" rx="19" ry="6" fill="#ffffff" opacity="0.5"/>
        <text class="icon-letter" x="32" y="28" text-anchor="middle" fill="var(--green-letter)">C</text>
      </svg>
      <span class="choice-label">Answer 3</span>
    </li>
    <li class="choice">
      <svg class="choice-icon" viewBox="0 0 64 40" aria-hidden="true">
        <defs>
          <radialGradient id="fill-d" cx="50%" cy="40%" r="60%">
            <stop offset="0" stop-color="var(--red-light)"/>
            <stop offset="1" stop-color="var(--red-mid)"/>
          </radialGradient>
        </defs>
        <ellipse cx="32" cy="20" rx="31" ry="19" fill="var(--red-ring)"/>
        <ellipse cx="32" cy="19" rx="26" ry="15" fill="url(#fill-d)"/>
        <ellipse cx="32" cy="12" rx="19" ry="6" fill="#ffffff" opacity="0.55"/>
        <text class="icon-letter" x="32" y="28" text-anchor="middle" fill="var(--red-letter)">D</text>
      </svg>
      <span class="choice-label">Answer 4</span>
    </li>
  </ul>
</main>
</body>
</html>
```